Lumo Ket

Need business cards designed. Project is an Arts Center in Hollywood. It'll include 3 live theatre, a restaurant and event space.

Target Market(s)

Across the board, young and old.

Industry/Entity Type

Entertainment

Contact Information for Business Card

Be creative. This is a creative venture that I'm building.

```html
<!DOCTYPE html>
<html lang="en">
<head>
<meta charset="utf-8">
<title>Lumo Ket — Business Card</title>
<link rel="stylesheet" href="https://fonts.googleapis.com/css2?family=Pinyon+Script&display=swap">
<style>
  :root {
    --sky: #8799c4;
    --cloud-light: #f1f3f9;
    --cloud-mid: #c3cde6;
    --brand-red: #a61f20;
    --rule-start: #c8262c;
    --rule-end: #3a1f1c;
    --disc-white: #ffffff;
    --disc-grey: #9a9a9a;
    --icon: #ffffff;
  }
  html, body {
    margin: 0;
    padding: 0;
    width: 1200px;
    height: 720px;
    overflow: hidden;
    background: var(--sky);
  }
  .card {
    position: relative;
    width: 1200px;
    height: 720px;
    background: var(--sky);
    overflow: hidden;
  }
  .cloud-photo {
    position: absolute;
    left: 110px;
    top: 170px;
    width: 1000px;
    height: 440px;
    background:
      radial-gradient(ellipse 38% 45% at 35% 55%, var(--cloud-light) 0%, var(--cloud-mid) 45%, rgba(135,153,196,0) 100%),
      radial-gradient(ellipse 30% 30% at 62% 40%, rgba(241,243,249,0.85) 0%, rgba(135,153,196,0) 100%);
  }
  .plane-sketch {
    position: absolute;
    left: 560px;
    top: 158px;
    width: 105px;
    height: 82px;
    background: radial-gradient(ellipse at center, rgba(255,255,255,0.35), rgba(255,255,255,0));
  }
  .emblem-disc {
    position: absolute;
    left: 620px;
    top: 139px;
    width: 322px;
    height: 308px;
  }
  .wordmark {
    position: absolute;
    margin: 0;
    font-family: "Pinyon Script", cursive;
    font-weight: 400;
    font-size: 128px;
    line-height: 1;
    color: var(--brand-red);
    white-space: nowrap;
  }
  .wordmark-left { left: 250px; top: 250px; }
  .wordmark-right { left: 690px; top: 232px; }
  .divider-rule {
    position: absolute;
    left: 80px;
    top: 450px;
    width: 1040px;
    height: 11px;
    background: linear-gradient(90deg, var(--rule-start), var(--brand-red) 50%, var(--rule-end));
  }
  .contact-icons {
    position: absolute;
    top: 462px;
    left: 0;
    width: 1200px;
    height: 50px;
  }
  .contact-icon {
    position: absolute;
    top: 0;
    fill: none;
    stroke: var(--icon);
    stroke-width: 3.2;
    stroke-linejoin: round;
    stroke-linecap: round;
  }
  .icon-mail { left: 324px; top: 14px; }
  .icon-phone { left: 585px; top: 2px; }
  .icon-pin { left: 836px; top: 0; }
</style>
</head>
<body>
  <main class="card">
    <div class="cloud-photo" role="img" aria-label="Photograph of soft white clouds in a blue sky"></div>
    <div class="plane-sketch" role="img" aria-label="Sketched paper airplane illustration"></div>

    <svg class="emblem-disc" viewBox="0 0 322 308" aria-hidden="true">
      <defs>
        <linearGradient id="discShade" x1="0" x2="1" y1="0" y2="0">
          <stop offset="0" stop-color="var(--disc-white)"/>
          <stop offset="0.45" stop-color="var(--disc-white)"/>
          <stop offset="1" stop-color="var(--disc-grey)"/>
        </linearGradient>
      </defs>
      <ellipse cx="161" cy="154" rx="161" ry="154" fill="url(#discShade)"/>
    </svg>

    <h1 class="wordmark wordmark-left">Lumo</h1>
    <span class="wordmark wordmark-right">Ket</span>

    <div class="divider-rule"></div>

    <div class="contact-icons">
      <svg class="contact-icon icon-mail" width="48" height="30" viewBox="0 0 48 30" aria-label="Email">
        <rect x="2" y="2" width="44" height="26"/>
        <polyline points="2,2 24,18 46,2"/>
      </svg>
      <svg class="contact-icon icon-phone" width="46" height="46" viewBox="0 0 46 46" aria-label="Phone">
        <path d="M30 4 l8 8 l-6 6 c-3 6 -8 11 -14 14 l-6 -6 l-8 8 c4 7 12 9 18 5 c8 -5 15 -12 20 -20 c4 -6 2 -14 -5 -18 z"/>
      </svg>
      <svg class="contact-icon icon-pin" width="34" height="44" viewBox="0 0 34 44" aria-label="Location">
        <path d="M17 42 C8 30 3 23 3 16 a14 14 0 0 1 28 0 c0 7 -5 14 -14 26 z"/>
        <circle cx="17" cy="16" r="6"/>
      </svg>
    </div>
  </main>
</body>
</html>
```